"Breathe & Bloom" Book Cover 5.5x8.5

Title of the book is "Breathe & Bloom"
Subtitle is "Unmasking Pricing Myths"
I've used PixelGuild on multiple occasions you can look on my Borvex page, Mark Delwitt, to see the covers I've used in the other projects I've done.
The target audience are people who have been tricked to think they can't retire because inflation, i.e. cost of living is going up so much they must work to keep up. There is no evidence of this.
And those are the people I want to reach so they can "Breathe...and Bloom."
Target Market(s)
Americans aged 55 and over who are thinking about retirement
Industry/Entity Type
Financial
Requirements
Nice to have
- Keep It Simple, Stupid is my mantra. Just make it pop out when people are browsing
Should not have
- No piggy banks. No old people sitting on a beach.

```html
<!DOCTYPE html>
<html lang="en">
<head>
<meta charset="UTF-8">
<title>Breathe &amp; Bloom — Book Cover</title>
<link rel="stylesheet" href="https://fonts.googleapis.com/css2?family=Montserrat:wght@300;400;700;800;900&display=swap">
<style>
  :root {
    --gold-light: #f6cd2e;
    --gold-mid: #e8b42b;
    --gold-dark: #d49e2a;
    --ink: #121212;
    --paper: #ffffff;
    --art-core: rgba(255, 255, 255, 0.62);
    --art-mid: rgba(250, 246, 235, 0.38);
    --art-edge: rgba(255, 244, 200, 0.14);
  }
  * { margin: 0; padding: 0; box-sizing: border-box; }
  html, body {
    width: 777px;
    height: 1200px;
    overflow: hidden;
  }
  body {
    background: var(--gold-dark);
    font-family: "Montserrat", sans-serif;
  }
  .cover {
    position: relative;
    width: 777px;
    height: 1200px;
    overflow: hidden;
    background: radial-gradient(ellipse 70% 55% at 50% 55%, var(--gold-light) 0%, var(--gold-mid) 55%, var(--gold-dark) 100%);
  }
  .title-block {
    position: absolute;
    top: 128px;
    left: 0;
    width: 100%;
    text-align: center;
  }
  .title {
    display: inline-block;
    text-align: left;
    color: var(--ink);
    font-weight: 900;
    text-transform: uppercase;
    line-height: 0.9;
    letter-spacing: -1px;
    padding-right: 46px;
  }
  .title-line {
    display: block;
    font-size: 106px;
  }
  .title-line--first {
    position: relative;
  }
  .title-amp {
    position: absolute;
    top: 6px;
    right: -50px;
    font-size: 58px;
    font-weight: 800;
    color: var(--paper);
    letter-spacing: 0;
  }
  .subtitle {
    position: absolute;
    top: 350px;
    left: 0;
    width: 100%;
    text-align: center;
    color: var(--paper);
    font-weight: 300;
    font-size: 34px;
    letter-spacing: 0.5px;
  }
  .cover-art {
    position: absolute;
    left: 110px;
    top: 455px;
    width: 557px;
    height: 545px;
    border-radius: 50%;
    background: radial-gradient(circle at 50% 50%, var(--art-core) 0%, var(--art-mid) 45%, var(--art-edge) 72%, rgba(255, 244, 200, 0) 74%);
  }
  .author {
    position: absolute;
    bottom: 42px;
    left: 0;
    width: 100%;
    text-align: center;
    color: var(--paper);
    font-weight: 700;
    font-size: 52px;
    letter-spacing: 1.5px;
    text-transform: uppercase;
  }
</style>
</head>
<body>
  <main class="cover">
    <div class="title-block">
      <h1 class="title">
        <span class="title-line title-line--first">Breathe<span class="title-amp">&amp;</span></span>
        <span class="title-line">Bloom</span>
      </h1>
    </div>
    <p class="subtitle">Unmasking Pricing Myths</p>
    <div class="cover-art" role="img" aria-label="Illustration of a person sitting cross-legged with a laptop, surrounded by small line icons of a megaphone, lightbulb, wallet, briefcase, charts, cash and a safe"></div>
    <p class="author">Mark Delwitt</p>
  </main>
</body>
</html>
```